Upmarket building and construction company needs signage

Our building company R Brent Construction, needs signage to put up on the side of our vehicle trailers and on site fencing. We are a building company that specialises in residential construction and carpentry .

I will attach our logo and some inspirational pics for site fencing as well as what our trailer looks like .
Other details i would like on the sign are our
( email) rbrentconstruction@mailbox-example.net
(mobile ) 0493 518 264
(website ) rbrentconstruction. example.net

Target Market(s)

Home owners looking for a reliable local builder who produces good quality work. I have attached some inspirational pics.

Industry/Entity Type

Building and Construction

Colors

Designer to choose colors to be used in the design.

Requirements
Must have
• Our logo, contact information
Nice to have
• We would like the design to have elements of being Elegant, Serious, Modern, Professional, Masculine, Conservative and Upmarket.

```html
<!DOCTYPE html>
<html lang="en">
<head>
<meta charset="utf-8">
<title>R Brent Construction – Signage</title>
<link href="https://fonts.googleapis.com/css2?family=Jost:wght@300;400&display=swap" rel="stylesheet">
<style>
  :root {
    --page: #ffffff;
    --sign-grey: #737371;
    --panel: #f0f0f0;
    --ink: #6d6d6b;
    --accent: #c8862a;
    --light: #ffffff;
  }
  * { margin: 0; padding: 0; box-sizing: border-box; }
  html, body { width: 1200px; height: 1200px; overflow: hidden; background: var(--page); }
  body { position: relative; font-family: "Jost", "Futura", sans-serif; color: var(--ink); }

  .sign { position: absolute; background: var(--sign-grey); overflow: hidden; }
  .sign--trailer { left: 115px; top: 214px; width: 978px; height: 367px; }
  .sign--fence { left: 255px; top: 627px; width: 698px; height: 366px; }

  .id-panel { position: absolute; left: 46px; top: 46px; width: 238px; height: 275px; background: var(--panel); z-index: 1; }
  .id-panel > * { position: absolute; left: 42px; white-space: nowrap; font-weight: 300; }
  .brand-name { top: 96px; font-size: 40px; line-height: 1; letter-spacing: 1px; color: var(--ink); font-weight: 300; }
  .brand-name span { display: block; }
  .brand-name .sub { font-size: 19.5px; letter-spacing: 2.2px; margin-top: 6px; }
  .tagline { top: 164px; font-size: 10.5px; letter-spacing: 1.3px; }
  .contact { top: 198px; font-size: 10.5px; line-height: 15px; }
  .contact .phone { font-size: 13px; letter-spacing: 0.5px; }

  .linework { position: absolute; left: 0; top: 0; width: 100%; height: 100%; z-index: 2; pointer-events: none; }
  .linework line { stroke: var(--accent); stroke-width: 1.2; }

  .skyline-area {
    position: absolute;
    background: linear-gradient(180deg, rgba(200, 134, 42, 0.05), rgba(200, 134, 42, 0.16));
  }
  .sign--trailer .skyline-area { left: 682px; top: 81px; width: 251px; height: 206px; }
  .sign--fence .skyline-area { left: 402px; top: 110px; width: 251px; height: 175px; }

  .services { position: absolute; color: var(--light); font-weight: 300; white-space: nowrap; text-transform: uppercase; }
  .services .sep { color: var(--accent); margin: 0 4px; }
  .sign--trailer .services { left: 315px; top: 244px; font-size: 15.5px; }
  .sign--fence .services { right: 46px; top: 40px; font-size: 21px; line-height: 23px; text-align: right; }
</style>
</head>
<body>

<section class="sign sign--trailer" aria-label="Trailer sign">
  <div class="id-panel">
    <h1 class="brand-name"><span>R BRENT</span><span class="sub">CONSTRUCTION</span></h1>
    <p class="tagline">BUILDING AND CARPENTRY</p>
    <p class="contact">rbrentconstruction@mailbox-example.net<br>rbrentconstruction.example.net<br><span class="phone">0493 518 264</span></p>
  </div>
  <p class="services">New Builds<span class="sep">|</span>Renovations<span class="sep">|</span>Residential<span class="sep">|</span>Commercial</p>
  <div class="skyline-area" role="img" aria-label="Orange line-art skyline of building outlines rising from the baseline"></div>
  <svg class="linework" viewBox="0 0 978 367" aria-hidden="true">
    <line x1="0" y1="287.5" x2="74" y2="287.5"/>
    <line x1="188" y1="287.5" x2="933" y2="287.5"/>
    <line x1="932.5" y1="287" x2="932.5" y2="367"/>
  </svg>
</section>

<section class="sign sign--fence" aria-label="Site fence sign">
  <div class="id-panel">
    <h2 class="brand-name"><span>R BRENT</span><span class="sub">CONSTRUCTION</span></h2>
    <p class="tagline">BUILDING AND CARPENTRY</p>
    <p class="contact">rbrentconstruction@mailbox-example.net<br>rbrentconstruction.example.net<br><span class="phone">0493 518 264</span></p>
  </div>
  <p class="services">New Builds<span class="sep">|</span>Renovations<br><span class="sep">|</span>Residential<span class="sep">|</span>Commercial</p>
  <div class="skyline-area" role="img" aria-label="Orange line-art skyline of building outlines rising from the baseline"></div>
  <svg class="linework" viewBox="0 0 698 366" aria-hidden="true">
    <line x1="0" y1="285.5" x2="74" y2="285.5"/>
    <line x1="187" y1="285.5" x2="653" y2="285.5"/>
    <line x1="652.5" y1="285" x2="652.5" y2="366"/>
  </svg>
</section>

</body>
</html>
```